Brenwick Winery Wine Label Re-design

Brenwick Winery is located in the Finger Lakes region of New York. The Brenwick Family planted the first vineyards in 1979 and opened in 1986. We produce award winning premium, hand crafted estate grown wines. We are in the process of a wine label re-design across our entire line. We would like to have the new label 'pop' but still convey elegance and ultra-premium quality. We are open to all color and styles or a minimalist design.
The attached files contain our new logo and samples of our current label (marked current) with dimensions. Our labeler is limited to label shapes but does not necessarily to have to be die-cut(the top arch) like our current label.

Target Market(s)

Upper income quality wine drinkers

Colors

Designer to choose colors to be used in the design.

Requirements
Should not have
• Should not be a tranparent label

```html
<!DOCTYPE html>
<html lang="en">
<head>
<meta charset="utf-8">
<title>Brenwick Winery – Wine Labels</title>
<link rel="stylesheet" href="https://fonts.googleapis.com/css2?family=Pinyon+Script&family=Montserrat:wght@400&family=Libre+Baskerville&family=Roboto+Condensed:wght@400&display=swap">
<style>
  :root {
    --backdrop-edge: #cfcdbf;
    --backdrop-mid: #f4f4f0;
    --label-black: #050505;
    --ink-white: #ffffff;
    --band-plum: #5a1838;
    --vine-green: #2e8a52;
    --vine-green-deep: #0f2a1b;
    --vine-red: #c0284f;
    --vine-red-deep: #35081a;
  }
  * { box-sizing: border-box; margin: 0; padding: 0; }
  html, body { width: 839px; height: 1200px; overflow: hidden; }
  body {
    position: relative;
    background: radial-gradient(ellipse at 50% 45%, var(--backdrop-mid) 0%, var(--backdrop-edge) 100%);
  }
  .label {
    position: absolute;
    top: 369px;
    width: 360px;
    height: 462px;
    background: var(--label-black);
    color: var(--ink-white);
    overflow: hidden;
  }
  .label--chardonnay { left: 40px; }
  .label--cabernet { left: 439px; }

  .vine-ornament {
    position: absolute;
    left: 0;
    top: 100px;
    width: 360px;
    height: 332px;
    opacity: 0.7;
  }
  .label--chardonnay .vine-ornament {
    background:
      radial-gradient(ellipse at 80% 12%, var(--vine-green) 0%, transparent 40%),
      radial-gradient(ellipse at 12% 20%, var(--vine-green) 0%, transparent 26%),
      radial-gradient(ellipse at 60% 88%, var(--vine-green) 0%, transparent 55%),
      var(--vine-green-deep);
  }
  .label--cabernet .vine-ornament {
    background:
      radial-gradient(ellipse at 80% 12%, var(--vine-red) 0%, transparent 40%),
      radial-gradient(ellipse at 12% 20%, var(--vine-red) 0%, transparent 26%),
      radial-gradient(ellipse at 60% 88%, var(--vine-red) 0%, transparent 55%),
      var(--vine-red-deep);
  }

  .winery-mark {
    position: absolute;
    top: 24px;
    left: 0;
    width: 100%;
    text-align: center;
    font-family: "Montserrat", sans-serif;
    font-weight: 400;
    color: var(--ink-white);
  }
  .winery-mark__circle {
    display: block;
    width: 30px;
    height: 30px;
    margin: 0 auto 8px;
    border: 2px solid var(--ink-white);
    border-radius: 50%;
  }
  .winery-mark__name {
    display: block;
    font-size: 22px;
    letter-spacing: 0.3em;
    line-height: 1;
    padding-left: 0.3em;
  }
  .winery-mark__sub {
    display: block;
    font-size: 12px;
    letter-spacing: 0.5em;
    margin-top: 3px;
    padding-left: 0.5em;
  }

  .varietal {
    position: absolute;
    top: 176px;
    left: 0;
    width: 100%;
    text-align: center;
    font-family: "Pinyon Script", cursive;
    font-weight: 400;
    font-size: 46px;
    line-height: 1;
    color: var(--ink-white);
    text-shadow: 0 0 6px rgba(0,0,0,0.9);
  }
  .vintage {
    position: absolute;
    top: 288px;
    left: 0;
    width: 100%;
    text-align: center;
    font-family: "Libre Baskerville", serif;
    font-size: 30px;
    color: var(--ink-white);
    text-shadow: 0 0 6px rgba(0,0,0,0.9);
  }
  .spec-band {
    position: absolute;
    left: 0;
    bottom: 0;
    width: 100%;
    height: 30px;
    background: var(--band-plum);
    display: flex;
    justify-content: space-between;
    align-items: center;
    padding: 0 12px;
    font-family: "Roboto Condensed", sans-serif;
    font-size: 13px;
    color: var(--ink-white);
  }
</style>
</head>
<body>
  <section class="label label--chardonnay">
    <div class="vine-ornament" role="img" aria-label="Engraved grape cluster and swirling vine leaves in green"></div>
    <div class="winery-mark">
      <span class="winery-mark__circle"></span>
      <span class="winery-mark__name">BRENWICK</span>
      <span class="winery-mark__sub">WINERY</span>
    </div>
    <h1 class="varietal">Reserve<br>Chardonnay</h1>
    <p class="vintage">2014</p>
    <div class="spec-band"><span>Alc. 15% BY VOL.</span><span>750ML</span></div>
  </section>

  <section class="label label--cabernet">
    <div class="vine-ornament" role="img" aria-label="Engraved grape cluster and swirling vine leaves in crimson"></div>
    <div class="winery-mark">
      <span class="winery-mark__circle"></span>
      <span class="winery-mark__name">BRENWICK</span>
      <span class="winery-mark__sub">WINERY</span>
    </div>
    <h1 class="varietal">Cabernet<br>Sauvignon</h1>
    <p class="vintage">2013</p>
    <div class="spec-band"><span>Alc. 15% BY VOL.</span><span>750ML</span></div>
  </section>
</body>
</html>
```